Pull Up Banners

Would like to have these pull up banner designs changed to a new modern theme. I have running a sales booth and want to re-design the banner designs. I have uploaded old banner design, I need phone number and website added onto bottom. Happy to consider images to attract people attention to increase sales and spark people interest walking past.

```html
<!DOCTYPE html>
<html lang="en">
<head>
<meta charset="utf-8">
<title>Northline – Cloud Phone System &amp; Internet Pull Up Banner</title>
<link rel="stylesheet" href="https://fonts.googleapis.com/css2?family=Montserrat:wght@400;500;700;800&display=swap">
<style>
  :root {
    --page-bg: #e6e6e6;
    --banner-black: #0b0b0b;
    --banner-white: #ffffff;
    --brand-orange: #ec5b1f;
    --text-light: #ffffff;
    --text-dark: #1b1b1b;
    --hero-olive: #4c5a34;
    --hero-lime: #b9c83a;
  }
  * { box-sizing: border-box; margin: 0; padding: 0; }
  html, body {
    width: 1141px; height: 1200px; overflow: hidden;
    background: var(--page-bg);
    font-family: "Montserrat", sans-serif;
  }
  .banner {
    position: absolute; left: 336px; top: 20px;
    width: 468px; height: 1160px;
    background: var(--banner-white);
    overflow: hidden;
  }
  .banner__dark-panel { position: absolute; left: 0; top: 0; width: 468px; height: 1160px; }
  .hero-photo {
    position: absolute; left: 0; top: 0; width: 468px; height: 380px;
    background:
      linear-gradient(180deg, rgba(11,11,11,0) 55%, var(--banner-black) 100%),
      linear-gradient(90deg, var(--banner-black) 0%, rgba(11,11,11,0.6) 35%, rgba(11,11,11,0) 70%),
      radial-gradient(ellipse at 80% 60%, var(--hero-lime) 0%, var(--hero-olive) 30%, #20241a 65%, var(--banner-black) 100%);
  }
  .brand {
    position: absolute; left: 41px; top: 46px;
    display: flex; align-items: center; gap: 14px;
  }
  .brand__dot {
    width: 44px; height: 44px; border-radius: 50%;
    background: var(--brand-orange);
  }
  .brand__text { display: flex; flex-direction: column; }
  .brand__name {
    font-weight: 500; font-size: 32px; letter-spacing: 3px;
    color: var(--brand-orange); line-height: 1;
  }
  .brand__tagline {
    margin-top: 5px; font-size: 7.5px; letter-spacing: 1.6px;
    color: var(--text-light); font-weight: 500;
  }
  .headline {
    position: absolute; left: 41px; top: 352px;
    color: var(--text-light); font-weight: 800;
    font-size: 39px; line-height: 48px; letter-spacing: 0.5px;
  }
  .headline__rule {
    position: absolute; left: 41px; top: 496px;
    width: 51px; height: 4px; background: var(--text-light);
  }
  .service {
    position: absolute; width: 150px; text-align: center;
    color: var(--text-light); font-size: 17px; line-height: 21px; font-weight: 400;
  }
  .service__icon {
    display: block; margin: 0 auto 14px;
    width: 80px; height: 80px;
  }
  .service--voip  { left: 28px;  top: 541px; }
  .service--sms   { left: 193px; top: 541px; }
  .service--teams { left: 28px;  top: 720px; }
  .service--net   { left: 193px; top: 720px; }
  .contact {
    position: absolute; left: 0; width: 468px; text-align: center;
    color: var(--text-dark); font-weight: 700;
  }
  .contact__phone { top: 1060px; font-size: 29px; }
  .contact__web   { top: 1098px; font-size: 25px; }
</style>
</head>
<body>
  <main class="banner">
    <svg class="banner__dark-panel" viewBox="0 0 468 1160" aria-hidden="true">
      <path d="M0,0 H468 V985 Q468,1040 395,1040 C240,1040 55,975 0,868 Z" fill="var(--banner-black)"/>
    </svg>

    <div class="hero-photo" role="img" aria-label="Photo of a hand touching a glowing screen with cloud and wifi line icons"></div>

    <header class="brand">
      <span class="brand__dot"></span>
      <div class="brand__text">
        <span class="brand__name">NORTHLINE</span>
        <span class="brand__tagline">THE NORTHLINE FOR ALL YOUR I.T SOLUTIONS</span>
      </div>
    </header>

    <h1 class="headline">CLOUD PHONE<br>SYSTEM &amp;<br>INTERNET</h1>
    <div class="headline__rule"></div>

    <section class="services">
      <div class="service service--voip">
        <svg class="service__icon" viewBox="0 0 80 80" aria-hidden="true">
          <circle cx="40" cy="40" r="38" fill="none" stroke="var(--brand-orange)" stroke-width="2"/>
          <path d="M27 24c2-2 5-2 6 1l3 6c1 2 0 4-2 5l-2 1c2 5 5 8 10 11l1-2c1-2 3-3 5-2l6 3c3 1 3 4 1 6l-3 3c-3 3-12 0-19-7s-10-16-8-19z" fill="var(--brand-orange)"/>
          <path d="M44 26a10 10 0 0 1 10 10M45 20a16 16 0 0 1 15 15M46 32a4 4 0 0 1 3 3" fill="none" stroke="var(--brand-orange)" stroke-width="2.5" stroke-linecap="round"/>
        </svg>
        VoIP &amp; Phone<br>Systems
      </div>
      <div class="service service--sms">
        <svg class="service__icon" viewBox="0 0 80 80" aria-hidden="true">
          <circle cx="40" cy="40" r="38" fill="none" stroke="var(--brand-orange)" stroke-width="2"/>
          <rect x="19" y="24" width="42" height="28" rx="4" fill="var(--brand-orange)"/>
          <path d="M27 52 L29 60 L35 52 Z" fill="var(--brand-orange)"/>
          <path d="M24 31h32M24 37h32M24 43h32" stroke="var(--banner-black)" stroke-width="2"/>
        </svg>
        SMS Gateway
      </div>
      <div class="service service--teams">
        <svg class="service__icon" viewBox="0 0 80 80" aria-hidden="true">
          <circle cx="40" cy="40" r="38" fill="none" stroke="var(--brand-orange)" stroke-width="2"/>
          <circle cx="40" cy="29" r="7" fill="var(--brand-orange)"/>
          <circle cx="25" cy="35" r="5" fill="var(--brand-orange)"/>
          <circle cx="55" cy="35" r="5" fill="var(--brand-orange)"/>
          <path d="M28 56c0-9 5-15 12-15s12 6 12 15z" fill="var(--brand-orange)"/>
          <path d="M16 56c0-8 4-12 9-12 2 0 3 1 4 1-2 3-3 7-3 11z" fill="var(--brand-orange)"/>
          <path d="M64 56c0-8-4-12-9-12-2 0-3 1-4 1 2 3 3 7 3 11z" fill="var(--brand-orange)"/>
        </svg>
        Teamlink<br>Calling
      </div>
      <div class="service service--net">
        <svg class="service__icon" viewBox="0 0 80 80" aria-hidden="true">
          <circle cx="40" cy="40" r="38" fill="none" stroke="var(--brand-orange)" stroke-width="2"/>
          <path d="M18 33a31 31 0 0 1 44 0M25 40a21 21 0 0 1 30 0M32 47a10 10 0 0 1 16 0" fill="none" stroke="var(--brand-orange)" stroke-width="5" stroke-linecap="round"/>
          <circle cx="40" cy="56" r="4" fill="var(--brand-orange)"/>
        </svg>
        NetGrid, Fibre &amp;<br>4G Internet
      </div>
    </section>

    <p class="contact contact__phone">08-5550-1234</p>
    <p class="contact contact__web">northlinecomputers.com.au</p>
  </main>
</body>
</html>
```